Fontenot Bayou Grillhouse (Owners Card)

Need a classy, but modern business card. I have included a promotional card for the steakhouse. I need one for myself (the owner) that is more professional.

Target Market(s)

General Public

Industry/Entity Type

Food service

Contact Information for Business Card

Name, business address, phone number, email, logo

Font styles to use
Serif
Sans Serif
Decorative
Script

Requirements
Must have
• My name (Darvel Pruitt), business address (327 Oakmere Street), phone number (510) 493-2615, email (Dpruittkr4@mailvane.example. On the back of the card: Psalms 27 1 The LORD is my light and my salvation— whom shall I fear? The LORD is the stronghold of my life— of whom shall I be afraid? 2 When the wicked advance against me to devour me, it is my enemies and my foes who will stumble and fall. 3 Though an army besiege me, my heart will not fear; though war break out against me, even then I will be confident.
Nice to have
• Something that’s bold, but modern and professional.

```html
<!DOCTYPE html>
<html lang="en">
<head>
<meta charset="utf-8">
<title>Fontenot Bayou Grillhouse — Owner's Card</title>
<link rel="stylesheet" href="https://fonts.googleapis.com/css2?family=Libre+Baskerville:wght@400;700&display=swap">
<style>
  :root {
    --stage: #e6e6e4;
    --card: #2d2d2d;
    --ghost: #353535;
    --ink: #f2f2f2;
    --green: #4caf2f;
    --gold: #e8a317;
    --orange: #f07818;
    --red: #e21b23;
    --edge: linear-gradient(90deg, var(--green), var(--gold) 50%, var(--red));
    --serif: "Libre Baskerville", "Times New Roman", serif;
  }
  * { box-sizing: border-box; margin: 0; padding: 0; }
  html, body { width: 1200px; height: 801px; overflow: hidden; }
  body {
    background: var(--stage);
    font-family: var(--serif);
    color: var(--ink);
    position: relative;
  }
  .card {
    position: absolute;
    top: 246px;
    width: 540px;
    height: 309px;
    background: var(--card);
    box-shadow: 0 10px 24px rgba(0,0,0,.22);
    overflow: hidden;
  }
  .card::after {
    content: "";
    position: absolute;
    left: 0; right: 0; bottom: 0;
    height: 4px;
    background: var(--edge);
  }
  .card--front { left: 45px; }
  .card--back { left: 615px; }

  /* front */
  .corner-chip {
    position: absolute; top: 0; right: 0;
    width: 26px; height: 12px;
    background: linear-gradient(90deg, var(--green), var(--gold));
  }
  .owner-name {
    position: absolute; top: 22px; right: 40px;
    font-size: 17px; font-weight: 700; letter-spacing: .5px;
    text-transform: uppercase;
    background: var(--edge);
    -webkit-background-clip: text; background-clip: text;
    color: transparent;
  }
  .ghost-mark {
    position: absolute; right: 40px; top: 70px;
    width: 210px; height: 210px; border-radius: 50%;
    background: var(--ghost);
  }
  .brand {
    display: flex; align-items: center; gap: 10px;
  }
  .brand__dot {
    width: 14px; height: 14px; border-radius: 50%;
    background: var(--orange); flex: none;
  }
  .brand__name {
    font-size: 19px; font-weight: 700; color: var(--orange);
    line-height: 1.2;
  }
  .card--front .brand { position: absolute; left: 34px; top: 104px; width: 240px; }
  .contact {
    position: absolute; left: 34px; top: 180px;
    font-size: 12.5px; line-height: 1.55;
  }
  .contact__address { margin-bottom: 12px; }
  .contact__row { display: flex; align-items: center; gap: 8px; }
  .contact__row svg { width: 13px; height: 13px; flex: none; }

  /* back */
  .card--back .brand {
    position: absolute; top: 58px; left: 0; right: 0; justify-content: center;
  }
  .card--back .brand__name { font-size: 24px; }
  .verses {
    position: absolute; left: 22px; right: 22px; top: 128px;
    list-style: none; font-size: 12.5px; line-height: 1.5; text-align: center;
  }
  .verses li { position: relative; padding-left: 26px; margin-bottom: 6px; }
  .verse-num {
    position: absolute; left: 0; top: 1px;
    width: 18px; height: 18px;
    border: 2px solid var(--green);
    display: grid; place-items: center;
    font-size: 11px; font-weight: 700; color: var(--gold);
    border-image: linear-gradient(135deg, var(--green), var(--red)) 1;
  }
</style>
</head>
<body>

<section class="card card--front" aria-label="Card front">
  <span class="corner-chip"></span>
  <h1 class="owner-name">Darvel Pruitt</h1>
  <div class="ghost-mark" role="img" aria-label="Faint brand emblem area"></div>
  <div class="brand">
    <span class="brand__dot"></span>
    <span class="brand__name">Fontenot Bayou Grillhouse</span>
  </div>
  <div class="contact">
    <p class="contact__address">327 Oakmere Street<br>Larkmont, CA 94871</p>
    <p class="contact__row">
      <svg viewBox="0 0 16 16" aria-hidden="true"><path d="M4 1.5l2.5 3-1.5 1.7c.8 1.8 2 3 3.8 3.8L10.5 8.5l3 2.5-1.5 3C6.5 14 2 9.5 2 3z" fill="var(--gold)"/></svg>
      (510) 493-2615
    </p>
    <p class="contact__row">
      <svg viewBox="0 0 16 16" aria-hidden="true"><rect x="1.5" y="3.5" width="13" height="9" fill="none" stroke="var(--orange)" stroke-width="1.5"/><path d="M1.5 3.5L8 9l6.5-5.5" fill="none" stroke="var(--orange)" stroke-width="1.5"/></svg>
      Dpruittkr4@mailvane.example
    </p>
  </div>
</section>

<section class="card card--back" aria-label="Card back">
  <div class="brand">
    <span class="brand__dot"></span>
    <span class="brand__name">Fontenot Bayou Grillhouse</span>
  </div>
  <ol class="verses">
    <li><span class="verse-num">1</span>Psalms 27 1 The LORD is my light and my salvation— whom shall I fear? The LORD is the stronghold of my life— of whom shall I be afraid?</li>
    <li><span class="verse-num">2</span>When the wicked advance against me to devour me, it is my enemies and my foes who will stumble and fall.</li>
    <li><span class="verse-num">3</span>Though an army besiege me, my heart will not fear; though war break out against me, even then I will be confident</li>
  </ol>
</section>

</body>
</html>
```